Loanharbor wedsite and logo refresh

We are looking for someone to refresh the look and feel of Loanharbor.co.nz we are moving it towards a more traditional brokerage.

Target Market(s)

30 to 55 year old professionals

Coding

Coded - Design and coding required

Number of Pages Required

3 page

Requirements
Nice to have
• we are needing a modern professional look

```html
<!DOCTYPE html>
<html lang="en">
<head>
<meta charset="utf-8">
<title>Loanharbor</title>
<link rel="stylesheet" href="https://fonts.googleapis.com/css2?family=Oswald:wght@300;400;500&family=Open+Sans:wght@400;600&family=Lato:wght@400&display=swap">
<style>
:root{
  --orange:#e8592b;
  --orange-soft:#ec7a4f;
  --ink:#2b2b2b;
  --grey:#6f6f6f;
  --dark:#1c1c1c;
  --white:#ffffff;
}
*{box-sizing:border-box;margin:0;padding:0}
html,body{width:1200px;height:3626px;overflow:hidden}
body{position:relative;font-family:"Open Sans",sans-serif;color:var(--ink);background:var(--white)}
.abs{position:absolute}
.display{font-family:"Oswald",sans-serif;font-weight:500;text-transform:uppercase;letter-spacing:-.5px}
.centered{left:0;width:1200px;text-align:center}
.pill{position:absolute;border-radius:30px;background:var(--orange);color:var(--white);display:flex;align-items:center;justify-content:center;font-size:17px;font-weight:600}

/* hero */
.hero{top:0;left:0;width:1200px;height:644px;background:linear-gradient(180deg,#4d5563 0%,#7a7a86 40%,#8a7468 62%,#3f4d5c 82%,#6e7f8c 100%)}
.brand-mark{left:111px;top:30px;font-family:"Oswald",sans-serif;font-weight:300;font-size:40px;color:var(--white);letter-spacing:-1px}
.nav{top:42px;font-family:"Oswald",sans-serif;font-size:19px;color:var(--white);text-transform:uppercase}
.nav a{position:absolute;white-space:nowrap;color:var(--white);text-decoration:none}
.nav a.active{color:var(--orange)}
.btn-login{left:832px;top:28px;width:122px;height:54px;border:2px solid var(--white);border-radius:30px;color:var(--white);font-size:18px;display:flex;align-items:center;justify-content:center;gap:8px}
.btn-signup{left:964px;top:28px;width:124px;height:54px;font-size:18px;font-weight:400;gap:8px}
.hero-title{top:155px;font-family:"Oswald",sans-serif;font-weight:400;font-size:126px;color:var(--white);line-height:1;letter-spacing:-3px}
.hero-tag{top:296px;font-size:31px;color:var(--white)}
.hero-cta{left:433px;top:360px;width:332px;height:68px;border:2px solid var(--white);border-radius:40px;color:var(--white);font-size:19px;font-weight:600;display:flex;align-items:center;justify-content:center}
.dots{top:571px;left:553px;display:flex;gap:9px}
.dots span{width:16px;height:16px;border-radius:50%;border:2px solid var(--white)}
.dots span:first-child{background:var(--white)}

/* welcome */
.welcome-kicker{left:111px;top:705px;font-size:46px;color:var(--ink)}
.welcome-name{left:111px;top:755px;font-size:60px;color:var(--orange)}
.welcome-copy{left:111px;top:860px;width:495px;font-family:"Lato",sans-serif;font-size:16.5px;line-height:29px;color:var(--grey)}
.welcome-copy p+p{margin-top:29px}
.video{left:647px;top:734px;width:441px;height:283px;background:linear-gradient(135deg,#1a4e78 0%,#3aa0d8 45%,#bfe6f6 100%);box-shadow:0 4px 14px rgba(0,0,0,.25)}
.btn-more{left:111px;top:1090px;width:166px;height:57px}

/* rates */
.rates{top:1210px;left:0;width:1200px;height:615px;background:linear-gradient(135deg,#d9582c 0%,#e77a4e 45%,#d9602f 100%)}
.rates-kicker{top:1252px;font-size:46px;color:var(--white)}
.rates-title{top:1303px;font-size:60px;color:var(--white)}
.rates-frame{left:112px;top:1410px;width:976px;height:357px;border:2px solid var(--white)}
.rates-divider{left:599px;top:1410px;width:2px;height:357px;background:var(--white)}
.rate-item{width:200px;text-align:center;color:var(--white);font-size:23px;line-height:30px}
.rate-card{left:478px;top:1449px;width:245px;height:279px;background:var(--white);text-align:center}
.rate-card h3{margin-top:131px;font-size:22px;font-weight:400;color:var(--ink)}
.rate-card p{margin-top:10px;font-size:15px;line-height:25px;color:var(--grey)}
.arrow-btn{width:40px;height:40px;border-radius:50%;background:var(--white);display:flex;align-items:center;justify-content:center}

/* why */
.why{top:1825px;left:0;width:1200px;height:678px;background:linear-gradient(90deg,#f3efec 0%,#fbfaf9 40%,#fbf9f7 60%,#efe8e2 100%)}
.why-kicker{top:1864px;font-size:46px;color:var(--ink)}
.why-title{top:1920px;font-size:60px;color:var(--orange)}
.why-photo{left:434px;top:2022px;width:332px;height:332px;border-radius:50%;border:9px solid #2f2f2f;background:radial-gradient(circle at 45% 45%,#f1d8c7 0%,#d9b39a 40%,#b7b8c2 100%)}
.feature-ring{width:84px;height:84px;border-radius:50%;border:4px solid #3a3a3a;background:var(--white);display:flex;align-items:center;justify-content:center}
.feature{width:270px}
.feature h4{font-size:20px;font-weight:400;color:var(--ink)}
.feature p{margin-top:10px;font-family:"Lato",sans-serif;font-size:15.5px;line-height:26px;color:var(--grey)}
.feature.left{text-align:right}
.btn-start{left:518px;top:2393px;width:164px;height:55px}

/* reviews */
.reviews-kicker{top:2553px;font-size:46px;color:var(--ink)}
.reviews-title{top:2609px;font-size:60px;color:var(--orange)}
.reviewer{left:112px;top:2691px;width:212px;height:212px;border-radius:50%;border:6px solid var(--orange);background:linear-gradient(160deg,#cfd9e3 0%,#b8c8d8 60%,#9fb2c6 100%)}
.review-rule{left:380px;top:2710px;width:2px;height:174px;background:#bdbdbd}
.review-text{left:440px;top:2712px;width:640px;font-family:"Lato",sans-serif;font-size:15.5px;line-height:29px;color:var(--grey)}
.review-name{left:441px;top:2850px;font-size:22px;color:var(--ink);letter-spacing:.5px}

/* contact */
.contact{top:2966px;left:0;width:1200px;height:660px;background:var(--dark)}
.contact-kicker{top:3012px;font-size:46px;color:var(--white);left:0;width:1130px}
.contact-title{top:3068px;font-size:60px;color:var(--orange);left:0;width:1130px}
.col-title{top:3172px;font-size:21px;color:var(--white)}
.field{border:1px solid #d6d6d6;color:var(--white);font-size:15.5px;padding:12px 14px}
.btn-submit{left:547px;top:3451px;width:131px;height:49px;font-size:18px}
.info-row{left:743px;display:flex;align-items:center;gap:18px;color:var(--white);font-size:16px;line-height:24px}
.icon-ring{width:34px;height:34px;border-radius:50%;border:1px solid var(--orange);display:flex;align-items:center;justify-content:center;flex:none}
.social{width:34px;height:34px;border-radius:50%;border:1px solid var(--orange)}
.footer-rule{left:75px;top:3536px;width:969px;height:1px;background:#555}
.copyright{top:3567px;left:0;width:1130px;text-align:center;color:var(--white);font-size:16px}
</style>
</head>
<body>

<!-- hero -->
<section class="abs hero" role="img" aria-label="City harbour skyline with a sailboat at dusk"></section>
<div class="abs brand-mark">LOANHARBOR</div>
<nav class="abs nav" aria-label="Main">
  <a class="active" style="left:467px">Home</a>
  <a style="left:542px">About</a>
  <a style="left:628px">Services</a>
  <a style="left:734px">Contact</a>
</nav>
<div class="abs btn-login">
  <svg width="12" height="14" viewBox="0 0 12 14"><rect x="1" y="6" width="10" height="8" rx="1" fill="#fff"/><path d="M3 6V4a3 3 0 0 1 6 0v2" stroke="#fff" stroke-width="2" fill="none"/></svg>LOGIN
</div>
<div class="pill btn-signup">
  <svg width="14" height="14" viewBox="0 0 14 14"><path d="M2 12l1-4 7-7 3 3-7 7z" fill="#fff"/></svg>SIGN UP
</div>
<h1 class="abs centered hero-title">LOANHARBOR</h1>
<div class="abs centered hero-tag">Put the power in the hands of the consumer</div>
<div class="abs hero-cta">FIND AND COMPARE RATES</div>
<div class="abs dots"><span></span><span></span><span></span><span></span></div>

<!-- welcome -->
<h2 class="abs display welcome-kicker">Welcome to</h2>
<h2 class="abs display welcome-name">Loanharbor</h2>
<div class="abs welcome-copy">
  <p>“Our goal is to get major banks, insurance companies, utility companies and other consumer service suppliers fighting for the consumer’s business.”</p>
  <p>With Loanharbor, you can submit a form with a few basic details, and get a range of representative offers back in under 90 seconds.</p>
</div>
<div class="abs video" role="img" aria-label="Hand with a pen over a blue financial bar and line chart"></div>
<svg class="abs" style="left:840px;top:848px" width="56" height="56" viewBox="0 0 56 56"><circle cx="28" cy="28" r="28" fill="#1b1b1b" opacity=".85"/><path d="M22 17l17 11-17 11z" fill="#fff"/></svg>
<div class="pill btn-more">READ MORE</div>

<!-- rates -->
<section class="abs rates" role="img" aria-label="Orange-toned desk with financial papers, a pen and a keyboard"></section>
<h2 class="abs display centered rates-kicker">Find and compare</h2>
<h2 class="abs display centered rates-title">Rates</h2>
<div class="abs rates-frame"></div>
<div class="abs rates-divider"></div>

<svg class="abs" style="left:160px;top:1490px" width="92" height="100" viewBox="0 0 92 100" fill="none" stroke="#fff" stroke-width="3"><path d="M20 40L50 10l30 30M28 32v30h44V32"/><circle cx="42" cy="40" r="4"/><circle cx="58" cy="54" r="4"/><path d="M40 58l20-20"/><path d="M4 70h16l16 8h24c6 0 6 8 0 8H40M20 92h40l26-18"/></svg>
<div class="abs rate-item" style="left:105px;top:1612px">Mortgage<br>Rates</div>

<svg class="abs" style="left:328px;top:1500px" width="86" height="90" viewBox="0 0 86 90" fill="none" stroke="#fff" stroke-width="3"><circle cx="22" cy="10" r="8"/><path d="M10 24h24v30h-6v32H16V54h-6z"/><text x="44" y="28" fill="#fff" stroke="none" font-size="30" font-family="Open Sans">$</text><path d="M40 82l14-18 10 8 18-22M74 50h8v8"/></svg>
<div class="abs rate-item" style="left:271px;top:1612px">Personal<br>Finance</div>

<div class="abs rate-card">
  <h3>Vehicle Finance</h3>
  <p>Let’s start the process<br>to find a vehicle finance<br>that works for you.</p>
</div>
<svg class="abs" style="left:555px;top:1470px" width="90" height="96" viewBox="0 0 90 96" fill="none" stroke="#e8592b" stroke-width="3"><circle cx="45" cy="20" r="17"/><text x="37" y="30" fill="#e8592b" stroke="none" font-size="26" font-family="Open Sans">$</text><path d="M14 62l8-18h46l8 18M8 62h74v22H8zM14 84v8h12v-8M64 84v8h12v-8"/><circle cx="20" cy="73" r="4"/><circle cx="70" cy="73" r="4"/><path d="M34 72h22"/></svg>

<svg class="abs" style="left:772px;top:1500px" width="90" height="88" viewBox="0 0 90 88" fill="none" stroke="#fff" stroke-width="3"><path d="M4 26L45 4l41 22zM10 30h70M10 80h70M4 86h82"/><path d="M16 34v40M74 34v40"/><rect x="26" y="36" width="38" height="38"/><text x="36" y="66" fill="#fff" stroke="none" font-size="28" font-family="Open Sans">$</text></svg>
<div class="abs rate-item" style="left:717px;top:1612px">Business &amp;<br>Asset Finance</div>

<svg class="abs" style="left:937px;top:1510px" width="104" height="90" viewBox="0 0 104 90" fill="none" stroke="#fff" stroke-width="3"><path d="M2 4h100M8 4v52h88V4"/><path d="M18 18h24M18 28h18M18 38h24"/><circle cx="72" cy="30" r="17"/><path d="M72 30V13M72 30l14 10"/><path d="M52 56v18"/><circle cx="52" cy="80" r="5" fill="#fff"/></svg>
<div class="abs rate-item" style="left:889px;top:1612px">Commercial<br>Finance</div>

<div class="abs arrow-btn" style="left:91px;top:1567px"><svg width="12" height="16" viewBox="0 0 12 16"><path d="M9 2L3 8l6 6" stroke="#333" stroke-width="2" fill="none"/></svg></div>
<div class="abs arrow-btn" style="left:1068px;top:1567px"><svg width="12" height="16" viewBox="0 0 12 16"><path d="M3 2l6 6-6 6" stroke="#333" stroke-width="2" fill="none"/></svg></div>

<!-- why -->
<section class="abs why" role="img" aria-label="Soft blurred office background with a pen"></section>
<h2 class="abs display centered why-kicker">Why</h2>
<h2 class="abs display centered why-title">Choose us</h2>
<div class="abs why-photo" role="img" aria-label="Close-up of a hand signing a document with a pen"></div>

<div class="abs feature-ring" style="left:376px;top:2038px"><svg width="36" height="30" viewBox="0 0 36 30"><path d="M2 28h32" stroke="#e8592b" stroke-width="2"/><rect x="5" y="14" width="4" height="12" fill="#e8592b"/><rect x="12" y="8" width="4" height="18" fill="#e8592b"/><rect x="19" y="16" width="4" height="10" fill="#e8592b"/><rect x="26" y="4" width="4" height="22" fill="#e8592b"/></svg></div>
<div class="abs feature-ring" style="left:737px;top:2038px"><svg width="24" height="28" viewBox="0 0 24 28"><path d="M12 1l10 4v8c0 7-5 11-10 14C7 24 2 20 2 13V5z" fill="#e8592b"/><path d="M12 5v18c3-2 6-5 6-10V8z" fill="#fff"/></svg></div>
<div class="abs feature-ring" style="left:369px;top:2237px"><svg width="28" height="28" viewBox="0 0 28 28"><circle cx="14" cy="14" r="13" fill="#e8592b"/><path d="M8 6c4 2 2 6 6 7s1 6 4 8M18 4c-1 3 2 4 5 5" stroke="#fff" stroke-width="2" fill="none"/></svg></div>
<div class="abs feature-ring" style="left:744px;top:2237px"><svg width="30" height="30" viewBox="0 0 30 30"><circle cx="15" cy="15" r="12" stroke="#e8592b" stroke-width="4" fill="none"/><path d="M7 23L23 7" stroke="#e8592b" stroke-width="4"/></svg></div>

<div class="abs feature left" style="left:86px;top:2022px"><h4>Great Rates &amp; Incentives</h4><p>Receive the great rates and incentives hassle-free - Loanharbor does the shopping around for you.</p></div>
<div class="abs feature left" style="left:86px;top:2229px"><h4>Any Time, Any Where</h4><p>Get notifications and review representative offers wherever you are with your personal, mobile -friendly Loanharbor dashboard.</p></div>
<div class="abs feature" style="left:844px;top:2022px"><h4>Privacy is Important</h4><p>Your private information is disclosed only when you follow up on representative offers from a service provider.</p></div>
<div class="abs feature" style="left:844px;top:2229px"><h4>No Fees, No Obligations</h4><p>The Loanharbor service is free and you are under no obligation until you select the representative offer that best suits your needs.</p></div>
<div class="pill btn-start">GET STARTED</div>

<!-- reviews -->
<h2 class="abs display centered reviews-kicker">Client</h2>
<h2 class="abs display centered reviews-title">Reviews</h2>
<div class="abs reviewer" role="img" aria-label="Portrait photo of a smiling client in a shirt and tie"></div>
<div class="abs review-rule"></div>
<p class="abs review-text">“ At vero eos et accusamus et iusto odio dignissimos ducimus qui blanditiis praesentium voluptat um deleniti atque corrupti quos dolores et quas molestias excepturi sint occae cati cupiditate non provident, similique sunt in culpa qui officia deserunt mollitia animi, id est laborum et dolorum fuga. “</p>
<div class="abs review-name">ROWAN VESEY</div>
<svg class="abs" style="left:58px;top:2781px" width="20" height="32" viewBox="0 0 20 32"><path d="M16 2L4 16l12 14" stroke="#777" stroke-width="2.5" fill="none"/></svg>
<svg class="abs" style="left:1113px;top:2781px" width="20" height="32" viewBox="0 0 20 32"><path d="M4 2l12 14L4 30" stroke="#777" stroke-width="2.5" fill="none"/></svg>

<!-- contact -->
<section class="abs contact"></section>
<h2 class="abs display centered contact-kicker">Contact us</h2>
<h2 class="abs display centered contact-title">Get in touch</h2>

<div class="abs col-title" style="left:74px">Request a Quote</div>
<div class="abs field" style="left:75px;top:3232px;width:294px;height:44px">Name :</div>
<div class="abs field" style="left:381px;top:3232px;width:294px;height:44px">Phone no :</div>
<div class="abs field" style="left:75px;top:3295px;width:600px;height:44px">Email :</div>
<div class="abs field" style="left:75px;top:3356px;width:600px;height:83px">Message :</div>
<div class="pill btn-submit">SUBMIT</div>

<div class="abs col-title" style="left:743px">Contact Information</div>
<div class="abs info-row" style="top:3219px">
  <div class="icon-ring"><svg width="12" height="16" viewBox="0 0 12 16"><path d="M6 15S1 9 1 6a5 5 0 0 1 10 0c0 3-5 9-5 9z" stroke="#e8592b" stroke-width="1.5" fill="none"/><circle cx="6" cy="6" r="1.8" fill="#e8592b"/></svg></div>
  <div>14 Kestrel Lane,<br>Harbourside 4829, New Zealand</div>
</div>
<div class="abs info-row" style="top:3304px">
  <div class="icon-ring"><svg width="14" height="14" viewBox="0 0 14 14"><path d="M3 1l3 3-2 2c1 2 2 3 4 4l2-2 3 3-2 2C6 13 1 8 1 3z" fill="#e8592b"/></svg></div>
  <div>0500 41 63 80</div>
</div>
<div class="abs info-row" style="top:3371px">
  <div class="icon-ring"><svg width="14" height="11" viewBox="0 0 14 11"><rect x="0" y="0" width="14" height="11" rx="1" fill="#e8592b"/><path d="M1 1l6 5 6-5" stroke="#1c1c1c" stroke-width="1.3" fill="none"/></svg></div>
  <div>info@loanharbor.co.nz</div>
</div>
<div class="abs social" style="left:744px;top:3433px"></div>
<div class="abs social" style="left:791px;top:3433px"></div>
<div class="abs social" style="left:837px;top:3433px"></div>

<div class="abs footer-rule"></div>
<div class="abs copyright">Copyright © 2020, Loanharbor. All rights reserved.</div>
<svg class="abs" style="left:1096px;top:3566px" width="30" height="18" viewBox="0 0 30 18"><path d="M2 16L15 3l13 13" stroke="#fff" stroke-width="3" fill="none"/></svg>

</body>
</html>
```